Halvorn - Refresh the look and feel of an existing website

We currently have an existing website www.halvornworldadvisory.example however it needs a more refreshed 'look and feel'. We are a professional consultancy that works with large corporate organisations and government. Our 'tag line' is A New Way of Thinking. We want the site to communicate "Innovation" and Leading Edge Thinking.

Target Market(s)

Corporate and Professional Clients - Organisation and Business Change

Industry/Entity Type

Management Consulting

Number of Pages Required

1 page

Font styles to use
Sans Serif

Requirements
Must have
• Must have a professional Corporate look and feel. Header 'imagery' is ok but boxes on front page need changing ... along with the words. The focus on home page needs to 'call out' 3 main consulting areas:-
• - Change & Transformation Specialists
• - Innovative Solutions
• - Digital Transformation
• Tag Line for business is ... A New Way of Thinking (Highlighting Halvorn as 'Thought Leaders' in business)
Nice to have
• Less "words' more imagery. Possibly an area for a 'video' or recent articles/blogs on the front page. Needs to have more of an 'interactive' feel. We are open to suggestions.
Should not have
• NA

```html
<!DOCTYPE html>
<html lang="en">
<head>
<meta charset="utf-8">
<title>Halvorn – A New Way of Thinking</title>
<link href="https://fonts.googleapis.com/css2?family=Lato:wght@400;700&family=Raleway:wght@500;700&family=Open+Sans:wght@400&display=swap" rel="stylesheet">
<style>
:root{
  --navy:#28425f;
  --navy-deep:#233b57;
  --header-bg:#eef0f3;
  --ink:#2b2b2b;
  --dark:#141414;
  --footer:#0a3a5b;
  --footer-icon:#1f6e9f;
  --white:#ffffff;
}
*{margin:0;padding:0;box-sizing:border-box}
html,body{width:1200px;height:1049px;overflow:hidden;background:var(--white)}
body{position:relative;font-family:'Lato',sans-serif;color:var(--ink)}
.site-header{position:absolute;left:0;top:0;width:1200px;height:104px;background:var(--header-bg)}
.brand{position:absolute;left:49px;top:14px;display:flex;align-items:center;gap:14px;height:72px}
.brand-mark{width:70px;height:70px;border-radius:50%;background:var(--navy)}
.brand-name{font-family:'Raleway',sans-serif;font-weight:500;font-size:34px;color:var(--navy);letter-spacing:1px}
.main-nav a{position:absolute;top:42px;font-size:14px;color:var(--ink);text-decoration:none;white-space:nowrap}
.main-nav .sep{position:absolute;top:41px;font-size:14px;color:var(--ink)}
.main-nav .home{top:0;left:347px;width:70px;height:104px;background:var(--navy);color:var(--white);font-weight:700;display:flex;align-items:center;justify-content:center;padding-top:2px}
.header-tools svg{position:absolute;top:43px}
.hero{position:absolute;left:0;top:104px;width:1200px;height:574px;overflow:hidden}
.hero-photo{position:absolute;inset:0;background:linear-gradient(100deg,#7f8a98 0%,#9aa4b1 35%,#b6bcc6 60%,#a7adb8 80%,#8e96a3 100%)}
.hero-shade{position:absolute;inset:0;background:rgba(40,55,80,.18)}
.hero-title{position:absolute;left:0;width:1200px;top:160px;text-align:center;font-family:'Raleway',sans-serif;font-weight:700;font-size:44px;color:var(--white)}
.hero-text{position:absolute;left:255px;width:690px;top:217px;text-align:center;font-size:15px;line-height:22.5px;color:var(--white)}
.hero-btn{position:absolute;left:539px;top:312px;width:133px;height:40px;background:var(--navy-deep);color:var(--white);font-size:14px;display:flex;align-items:center;justify-content:center;text-decoration:none}
.hero-arrow{position:absolute;top:198px}
.services{position:absolute;left:0;top:678px;width:1200px;height:292px;background:var(--dark);border-top:4px solid var(--white)}
.service{position:absolute;top:0;width:280px;text-align:center;color:var(--white)}
.service-badge{position:absolute;top:-68px;left:69px;width:142px;height:142px;border-radius:50%;background:var(--navy);border:3px solid var(--white);display:flex;align-items:center;justify-content:center}
.service h2{position:absolute;left:0;width:280px;font-family:'Raleway',sans-serif;font-weight:500;font-size:21px;line-height:23px}
.service p{position:absolute;left:10px;width:260px;top:150px;font-family:'Open Sans',sans-serif;font-size:12.5px;line-height:17px;color:#e6e6e6}
.service .more{position:absolute;left:0;width:280px;top:216px;font-size:13px;color:var(--white);text-decoration:none}
.site-footer{position:absolute;left:0;top:970px;width:1200px;height:79px;background:var(--footer)}
.copyright{position:absolute;left:50px;top:30px;font-size:13px;color:var(--white);letter-spacing:-.2px}
.social span{position:absolute;top:33px;width:13px;height:13px;border-radius:50%;background:var(--footer-icon)}
</style>
</head>
<body>
<header class="site-header">
  <div class="brand"><span class="brand-mark"></span><span class="brand-name">HALVORN</span></div>
  <nav class="main-nav">
    <a class="home" href="#">Home</a>
    <a href="#" style="left:455px">About Us</a><span class="sep" style="left:536px">|</span>
    <a href="#" style="left:563px">Our Services</a><span class="sep" style="left:661px">|</span>
    <a href="#" style="left:690px">Solutions</a><span class="sep" style="left:772px">|</span>
    <a href="#" style="left:798px">What's Happening</a><span class="sep" style="left:933px">|</span>
    <a href="#" style="left:958px">Contact Us</a>
  </nav>
  <div class="header-tools">
    <svg style="left:1066px" width="14" height="12" viewBox="0 0 14 12"><rect x="0" y="1" width="14" height="10" fill="#1a1a1a"/><path d="M0 1 L7 6 L14 1" stroke="#eef0f3" stroke-width="1.4" fill="none"/></svg>
    <svg style="left:1101px" width="14" height="14" viewBox="0 0 14 14"><circle cx="5.5" cy="5.5" r="4" stroke="#1a1a1a" stroke-width="2" fill="none"/><path d="M8.5 8.5 L13 13" stroke="#1a1a1a" stroke-width="2.4"/></svg>
    <svg style="left:1136px" width="12" height="13" viewBox="0 0 12 13"><circle cx="6" cy="3.5" r="3.2" fill="#1a1a1a"/><path d="M0 13 Q0 7 6 7 Q12 7 12 13Z" fill="#1a1a1a"/></svg>
  </div>
</header>

<section class="hero">
  <div class="hero-photo" role="img" aria-label="Photo of a consultant's hands writing, with a sketched lightbulb idea on paper"></div>
  <div class="hero-shade"></div>
  <h1 class="hero-title">Consectetur Adipiscing Elit</h1>
  <p class="hero-text">Lorem ipsum dolor sit amet, consectetur adipiscing elit, sed do eiusmod tempor incididunt ut labore et dolore magna aliqua. Ut enim ad minim veniam, quis nostrud exercitation ullamco laboris nisi ut aliquip ex ea commodo consequat</p>
  <a class="hero-btn" href="#">READ MORE</a>
  <svg class="hero-arrow" style="left:27px" width="20" height="64" viewBox="0 0 20 64"><path d="M18 1 L2 32 L18 63" stroke="#fff" stroke-width="1.5" fill="none"/></svg>
  <svg class="hero-arrow" style="left:1148px" width="20" height="64" viewBox="0 0 20 64"><path d="M2 1 L18 32 L2 63" stroke="#fff" stroke-width="1.5" fill="none"/></svg>
</section>

<section class="services">
  <article class="service" style="left:105px">
    <div class="service-badge">
      <svg width="80" height="80" viewBox="0 0 80 80"><path d="M14 40 A26 26 0 0 1 62 26" stroke="#fff" stroke-width="7" fill="none"/><path d="M56 16 L70 26 L56 34Z" fill="#fff"/><path d="M66 40 A26 26 0 0 1 18 54" stroke="#fff" stroke-width="7" fill="none"/><path d="M24 64 L10 54 L24 46Z" fill="#fff"/><circle cx="40" cy="36" r="7" fill="#fff"/><path d="M28 54 Q28 45 40 45 Q52 45 52 54Z" fill="#fff"/></svg>
    </div>
    <h2 style="top:100px">Change &amp; Transformation Specialists</h2>
    <p>Lorem ipsum dolor sit amet, consectetur adipiscing elit, sed do eiusmod tempor incidi-dunt ut labore et dolore magna aliqua.</p>
    <a class="more" href="#">MORE &#9656;</a>
  </article>
  <article class="service" style="left:466px">
    <div class="service-badge">
      <svg width="80" height="80" viewBox="0 0 80 80"><circle cx="40" cy="28" r="11" stroke="#fff" stroke-width="3" fill="none"/><rect x="35" y="38" width="10" height="6" fill="#fff"/><g stroke="#fff" stroke-width="2.5"><path d="M40 6 V12"/><path d="M22 12 L26 16"/><path d="M58 12 L54 16"/><path d="M16 28 H22"/><path d="M58 28 H64"/></g><path d="M14 72 Q14 50 40 50 Q66 50 66 72Z" fill="#fff"/></svg>
    </div>
    <h2 style="top:114px">Innovative Solutions</h2>
    <p>Lorem ipsum dolor sit amet, consectetur adipiscing elit, sed do eiusmod tempor incidi-dunt ut labore et dolore magna aliqua. Ut</p>
    <a class="more" href="#">MORE &#9656;</a>
  </article>
  <article class="service" style="left:817px">
    <div class="service-badge">
      <svg width="96" height="70" viewBox="0 0 96 70"><rect x="4" y="12" width="36" height="34" rx="4" stroke="#fff" stroke-width="4" fill="none"/><rect x="48" y="6" width="44" height="34" stroke="#fff" stroke-width="4" fill="none"/><rect x="66" y="40" width="8" height="10" fill="#fff"/><rect x="58" y="50" width="24" height="4" fill="#fff"/><path d="M30 30 Q44 18 58 26" stroke="#fff" stroke-width="3" fill="none"/><path d="M56 20 L64 27 L54 31Z" fill="#fff"/></svg>
    </div>
    <h2 style="top:114px">Digital Transformation</h2>
    <p>Lorem ipsum dolor sit amet, consectetur adipiscing elit, sed do eiusmod tempor incidi-dunt ut labore et dolore magna aliqua.</p>
    <a class="more" href="#">MORE &#9656;</a>
  </article>
</section>

<footer class="site-footer">
  <p class="copyright">All Rights Reserved. Copyrights @ company Name. 2016</p>
  <div class="social">
    <span style="left:982px"></span><span style="left:1022px"></span><span style="left:1059px"></span><span style="left:1096px"></span><span style="left:1134px"></span>
  </div>
</footer>
</body>
</html>
```